Silver Lantern Subscription Box Design, with Greeting Card, Booklet and Web Banners.

We need a PRINT READY box design with theme: ITALY
(Inner and outer sides)
The box contains Food & Beverage products coming directly from Italy.

Size: 80cmx35cmx16cm (attached for template). Yes, it's a big box, it has the wow factor, see the Vimbly screenshot example - referring to the size only - it has the wow unboxing factor.

ONCE WE AGREE ON THE BOX DESIGN, we then need the below deliverables using the design adaptation from the Box:
- Greeting card
- 12-page booklet (See Tovel*ra examples) - photos and copy will be provided.
- 3x Web/App Banners (See T*ve*lra examples) - the elements will need to be able to be used across different banner dimensions/sizes (a square, rectangle, etc. so for product hero shot, cover image, banner ads, story image, image listing, blog image, etc.).

The booklet structure is as follows:
(Total 1,000 words)
- Cover page
- (2 page spread) Intro 200 words max + Main Image
- A map indicating product origins
- (Across 5 pages) 2 products per page, 50-75 words each product + image
- (2 page spread) Community Development Innitiatives - 200 words max, a few images
- Back cover

After Italy, we will be doing India, China, Japan, Thailand, Mexico and Greece. So please keep in mind when designing the Italy Box as we need to allow a nice colour palette for the Silver Lantern range.

Our company logo and other details will be provided.
Cheers

Industry/Entity Type

Tech, F&B, Travel

Requirements
Must have
• Style: Clean, minimalistic, sophisticated, a mix of contemporary & Traditional, and sustainable. Imagine receiving and unboxing an Oxlet product, we need the same wow effect. On the outside: we need to have the App Logo (attached with the colour code), along with 3x small USP icons (Australian Owned, HACCP certified, and Recyclable), and small text: "Country of Origin: ITALY". You can adjust the colour of the icons to suit. We also need to be deliberate and bold with our messaging for "EAT ORIGINAL. PRESERVE HERITAGE", so we need this text either on the outer or inner of the box. Due to size of the box, placing this slogan on the inside when customer is unboxing may be ideal. Also on the inside: The usual social sharing icons with hashtag info. Feel free to add an instruction icons on how to unbox - in order to deliver an unmatched immersive experience.
Nice to have
• Background illustration graphics on Italian heritage/landmark buildings, towers, etc is an option. ANOTHER EXAMPLE: Just to give an example of a cool box design, though we need to stick to the Box Style brief above, is from Plimb - see attached.
Should not have
• Busy design, too flashy, graphics that are not representative of an Italian range.

```html
<!DOCTYPE html>
<html lang="en">
<head>
<meta charset="utf-8">
<title>Silver Lantern Italy Box – Inside Dieline</title>
<link rel="stylesheet" href="https://fonts.googleapis.com/css2?family=Figtree:wght@400;500;600;800&display=swap">
<style>
  :root {
    --green: #3d7a5c;
    --board: #efece6;
    --paper: #ffffff;
    --flag-red: #e56e5e;
    --bleed: #d6ead2;
    --trim: #2a2f6b;
    --crease: #d83a3a;
    --ink: #222222;
  }
  html, body {
    margin: 0;
    padding: 0;
    width: 1200px;
    height: 983px;
    overflow: hidden;
    background: var(--paper);
  }
  .dieline {
    display: block;
    width: 1200px;
    height: 983px;
    font-family: "Figtree", sans-serif;
  }
  .panel { fill: var(--board); }
  .bleed-line { fill: none; stroke: var(--bleed); stroke-width: 2; }
  .crop-mark { stroke: #555; stroke-width: 1.5; fill: none; }
  .side-label { fill: var(--green); font-size: 56px; font-weight: 500; }
  .spec { fill: var(--ink); font-size: 5px; font-weight: 500; }
  .headline { fill: var(--green); font-size: 79px; font-weight: 800; letter-spacing: -2px; }
  .closing { fill: var(--green); font-size: 82px; font-weight: 500; text-anchor: middle; }
  .closing .strong { font-weight: 800; }
  .web { fill: var(--green); font-size: 24px; font-weight: 600; text-anchor: middle; }
  .outer-note { fill: var(--ink); font-size: 8px; font-weight: 600; text-anchor: middle; }
  .flag-green { fill: var(--green); }
  .flag-white { fill: var(--paper); }
  .flag-red { fill: var(--flag-red); }
  .landmarks { fill: var(--green); opacity: 0.85; }
</style>
</head>
<body>
<svg class="dieline" viewBox="0 0 2000 1638" xmlns="http://www.w3.org/2000/svg">

  <!-- spec table -->
  <g class="spec-table">
    <text class="spec" x="108" y="5">Inside size</text>
    <text class="spec" x="108" y="11">Outside size</text>
    <text class="spec" x="108" y="17">Maker size</text>
    <text class="spec" x="108" y="23">Material</text>
    <text class="spec" x="108" y="29">Thickness</text>
    <text class="spec" x="108" y="35">BLEED</text>
    <line x1="127" y1="34" x2="147" y2="34" stroke="#5fb84a" stroke-width="2"/>
    <text class="spec" x="170" y="5">800x350x160 mm</text>
    <text class="spec" x="170" y="11">816x364x183 mm</text>
    <text class="spec" x="170" y="17">816x350x162 mm</text>
    <text class="spec" x="170" y="23">E-flute paper</text>
    <text class="spec" x="170" y="29">1.5mm</text>
    <text class="spec" x="170" y="35">TRIM</text>
    <line x1="185" y1="34" x2="205" y2="34" stroke="var(--trim)" stroke-width="2"/>
    <text class="spec" x="233" y="5">Remark</text>
    <text class="spec" x="233" y="11">Box No.</text>
    <text class="spec" x="233" y="17">Design Area</text>
    <text class="spec" x="233" y="23">Membrane</text>
    <text class="spec" x="224" y="35">CREASE</text>
    <line x1="224" y1="40" x2="244" y2="40" stroke="var(--crease)" stroke-width="2"/>
    <text class="spec" x="285" y="11">189610</text>
    <text class="spec" x="285" y="17">1479mm x 1186mm</text>
    <text class="spec" x="285" y="23">None</text>
  </g>

  <!-- crop marks -->
  <path class="crop-mark" d="M52 50 V56 H58 M1948 50 V56 H1942 M52 1586 V1580 H58 M1948 1586 V1580 H1942"/>

  <text class="side-label" x="46" y="143">Inside</text>

  <!-- bleed outline -->
  <path class="bleed-line" d="M480 56 H1520 C1640 60 1705 140 1705 215 C1705 255 1690 272 1720 272 V720 H1700 V915 H1942 V1376 H1700 V1580 H300 V1376 H57 V915 H300 V720 H279 V272 H310 C295 262 295 240 296 215 C296 140 360 60 480 56 Z"/>

  <!-- board panels -->
  <path class="panel" d="M485 64 H1515 C1625 68 1695 140 1695 220 C1695 250 1680 268 1650 268 H350 C320 268 305 250 305 220 C305 140 375 68 485 64 Z"/>
  <path class="panel" d="M490 268 H1510 V718 H490 Z"/>
  <path class="panel" d="M490 270 L300 338 Q286 344 286 360 V630 Q286 645 300 650 L490 718 Z"/>
  <path class="panel" d="M1510 270 L1700 338 Q1714 344 1714 360 V630 Q1714 645 1700 650 L1510 718 Z"/>
  <rect class="panel" x="305" y="718" width="1390" height="205"/>
  <rect class="panel" x="68" y="923" width="1862" height="445"/>
  <rect class="panel" x="63" y="990" width="10" height="60"/>
  <rect class="panel" x="63" y="1115" width="10" height="60"/>
  <rect class="panel" x="63" y="1243" width="10" height="60"/>
  <rect class="panel" x="1927" y="990" width="10" height="60"/>
  <rect class="panel" x="1927" y="1115" width="10" height="60"/>
  <rect class="panel" x="1927" y="1243" width="10" height="60"/>
  <rect class="panel" x="307" y="1368" width="1386" height="205"/>

  <!-- Italian flag -->
  <g class="flag">
    <rect class="flag-green" x="1405" y="268" width="23" height="127"/>
    <rect class="flag-white" x="1428" y="268" width="23" height="127"/>
    <rect class="flag-red" x="1451" y="268" width="23" height="127"/>
  </g>

  <!-- slogan -->
  <text class="headline" x="528" y="378">EAT ORIGINAL.</text>
  <text class="headline" x="528" y="465">PRESERVE HERITAGE</text>

  <!-- landmark illustration area -->
  <rect class="landmarks" x="665" y="480" width="810" height="443" rx="4" role="img" aria-label="Silhouette illustration of the Colosseum and the Leaning Tower of Pisa"/>

  <!-- closing message -->
  <text class="closing" x="998" y="1120">Want more? You</text>
  <text class="closing" x="998" y="1208">know <tspan class="strong">where</tspan> to find us</text>
  <text class="web" x="998" y="1310">www.silverlantern.io</text>

  <text class="outer-note" x="999" y="1600">Outer</text>
</svg>
</body>
</html>
```